Rivolex.com Trucking Company Website

Need a website designed (no content) for a trucking company, specializing in trucking of ocean containers (intermodal Trucking). Heavy emphasis on technology, using latest technology, providing unabated visibility and realtime information.
clean minimalist industrial website
example:
https://www.bramtiq.com/

Target Market(s)

Professional Business Consumer corporate and small business

Industry/Entity Type

Trucking Company

Number of Pages Required

5+ page

Requirements
Must have
• Industrial Design, simple informative, for a busy professional to view and get the necessary information with out the distractions.
• Blog Page
• Client Log-In on the front page
• Technology page - showing our intensive investments in technology
Nice to have
• If ANY images included, MUST be USA related. Example if include an image of a truck, ensure its a USA model. Do the research.
• included our business card for sample of Logo
• Doesnt not have to be the same color schemes.
Should not have
• moving images

```html
<!DOCTYPE html>
<html lang="en">
<head>
<meta charset="utf-8">
<title>Rivolex Consulting — Trucking &amp; Logistics</title>
<link rel="stylesheet" href="https://fonts.googleapis.com/css2?family=Lato:wght@400;700;900&family=Open+Sans:wght@400;600;700&display=swap">
<style>
:root{
  --brand:#1c4f8c;
  --brand-dark:#173a66;
  --hero-blue:#2f6db4;
  --navy:#1f3654;
  --ink:#222831;
  --text:#444b55;
  --panel:#2b323c;
  --footer:#262b32;
  --footer-deep:#1d2126;
  --muted:#a7adb5;
  --partner:#b9bcc0;
  --white:#ffffff;
}
*{box-sizing:border-box;margin:0;padding:0}
html,body{width:1200px;height:2862px;overflow:hidden}
body{position:relative;background:var(--white);font-family:"Open Sans",Arial,sans-serif;color:var(--text)}

/* header */
.site-header{position:absolute;left:0;top:0;width:1200px;height:105px;border-bottom:1px solid #e2e5ea;background:var(--white)}
.brand{position:absolute;left:92px;top:26px;font-family:"Lato",sans-serif;font-weight:900;font-size:44px;letter-spacing:2px;color:var(--brand);line-height:1}
.topbar{position:absolute;top:16px;right:96px;display:flex;gap:34px;align-items:center;font-family:"Lato",sans-serif;font-size:15px;color:var(--ink)}
.topbar span{display:flex;align-items:center;gap:10px}
.topbar .login{color:var(--brand);font-weight:700;letter-spacing:1px}
.main-nav{position:absolute;top:66px;right:96px;display:flex;gap:38px;font-family:"Lato",sans-serif;font-weight:700;font-size:15px;letter-spacing:1.4px;color:var(--ink)}
.main-nav .active{color:var(--brand)}

/* hero */
.hero{position:absolute;left:0;top:105px;width:1200px;height:601px;background:var(--hero-blue);overflow:hidden}
.hero-photo{position:absolute;inset:0;clip-path:polygon(639px 0,1200px 0,1200px 601px,454px 601px);background:linear-gradient(180deg,#a9c3dc 0%,#8fa98a 34%,#aab3ba 58%,#8e9399 100%)}
.hero-mark{position:absolute;left:604px;top:470px;font-family:"Lato",sans-serif;font-weight:900;font-size:64px;letter-spacing:4px;color:var(--brand)}
.hero-copy{position:absolute;left:95px;top:188px;font-family:"Lato",sans-serif;font-size:25px;line-height:38px;letter-spacing:.8px;color:var(--white)}
.quote-btn{position:absolute;left:92px;top:376px;width:217px;height:48px;border-radius:24px;background:var(--navy);color:var(--white);display:flex;align-items:center;gap:14px;padding-left:22px;font-family:"Lato",sans-serif;font-weight:700;font-size:16px;letter-spacing:.6px}

/* welcome */
.welcome{position:absolute;left:0;top:706px;width:1200px;height:382px;text-align:center}
.section-title{font-family:"Lato",sans-serif;font-weight:700;font-size:28px;letter-spacing:.6px}
.welcome .section-title{position:absolute;top:56px;width:100%;color:var(--ink)}
.welcome .section-title b{color:var(--brand)}
.divider{position:absolute;left:0;width:100%;display:flex;justify-content:center;align-items:center;gap:18px}
.divider i{display:block;width:94px;height:3px;background:currentColor}
.welcome .divider{top:110px;color:var(--ink)}
.welcome p{position:absolute;left:100px;width:1000px;font-size:15px;line-height:23px;color:var(--text)}
.welcome .mission{top:163px}
.welcome .priority{top:238px;font-weight:700;color:var(--ink)}
.pill-btn{position:absolute;left:490px;top:298px;width:218px;height:48px;border-radius:24px;background:var(--brand-dark);color:var(--white);font-family:"Lato",sans-serif;font-weight:700;font-size:16px;letter-spacing:2px;line-height:48px}

/* solutions */
.solutions{position:absolute;left:0;top:1088px;width:1200px;height:694px;overflow:hidden;background:linear-gradient(180deg,#4a6a8f 0%,#36577f 45%,#405f84 100%)}
.solutions .scene{position:absolute;inset:0;background:linear-gradient(180deg,rgba(130,155,185,.25),rgba(40,70,110,.08) 55%,rgba(90,110,130,.28))}
.solutions .section-title{position:absolute;top:56px;width:100%;text-align:center;color:var(--white)}
.solutions .divider{top:112px;color:var(--white)}
.hub{position:absolute;left:467px;top:286px;width:252px;height:252px;border-radius:50%;background:var(--white);display:flex;align-items:center;justify-content:center;font-family:"Lato",sans-serif;font-weight:900;font-size:46px;letter-spacing:2px;color:var(--brand)}
.service{position:absolute;width:200px;margin-left:-100px;text-align:center;color:var(--white);font-family:"Lato",sans-serif;font-weight:700;font-size:16px;letter-spacing:1.2px}
.service .ring{width:76px;height:76px;margin:0 auto 14px;border:3px solid var(--white);border-radius:50%;display:flex;align-items:center;justify-content:center}

/* sectors */
.sectors{position:absolute;left:0;top:1782px;width:1200px;height:521px}
.sectors-panel{position:absolute;left:0;top:0;width:614px;height:521px;background:var(--panel);color:var(--white)}
.sectors-panel h2{position:absolute;left:92px;top:62px;font-family:"Lato",sans-serif;font-weight:700;font-size:24px;letter-spacing:1px}
.sectors-panel .rule{position:absolute;left:92px;top:109px;width:96px;height:3px;background:var(--white)}
.sectors-panel .lead{position:absolute;left:92px;top:140px;width:470px;font-size:13.5px;font-weight:700;line-height:22px}
.sector-list{position:absolute;left:98px;top:196px;list-style:none}
.sector-list li{display:flex;align-items:center;gap:22px;height:56px;font-family:"Lato",sans-serif;font-weight:700;font-size:17px;letter-spacing:.6px}
.sector-list svg{width:40px;height:36px}
.sectors-photo{position:absolute;left:614px;top:0;width:586px;height:521px;background:linear-gradient(180deg,#8aa6c4 0%,#c4cfd9 40%,#6d7074 72%,#4a4d51 100%)}
.notch{position:absolute;left:598px;top:242px;width:0;height:0;border-top:16px solid transparent;border-bottom:16px solid transparent;border-right:16px solid var(--white)}

/* partners */
.partners{position:absolute;left:0;top:2303px;width:1200px;height:168px;background:#f4f5f6}
.partner{position:absolute;top:62px;height:44px;background:var(--partner);border-radius:4px;opacity:.8}

/* footer */
.site-footer{position:absolute;left:0;top:2471px;width:1200px;height:337px;background:var(--footer);color:var(--muted)}
.col{position:absolute;top:50px;width:260px}
.col h3{font-family:"Lato",sans-serif;font-weight:700;font-size:14px;letter-spacing:.5px;color:var(--white);margin-bottom:20px}
.col p{font-size:12.5px;line-height:21px}
.col ul{list-style:none}
.col li{font-size:12.5px;line-height:30.5px}
.col li::before{content:"›";color:var(--white);margin-right:8px}
.newsletter-form{position:absolute;left:0;top:133px;width:249px;height:36px;display:flex}
.newsletter-form .field{flex:1;background:#4a5059;color:#9aa1a9;font-size:12px;line-height:36px;padding-left:14px;font-style:italic}
.newsletter-form .send{width:36px;background:#1f73c6;display:flex;align-items:center;justify-content:center}
.contact .phone{font-weight:700;color:var(--white);font-size:16px;letter-spacing:.6px;margin-top:2px}
.contact .mail{color:var(--white);font-weight:600}
.socials{display:flex;gap:6px;margin-top:16px}
.socials i{display:block;width:40px;height:40px;background:#4a5059}
.copyright{position:absolute;left:0;top:2808px;width:1200px;height:54px;background:var(--footer-deep);color:var(--white);text-align:center;line-height:54px;font-size:14px;font-weight:600;letter-spacing:.5px}
</style>
</head>
<body>

<header class="site-header">
  <div class="brand">RIVOLEX</div>
  <div class="topbar">
    <span>
      <svg width="20" height="20" viewBox="0 0 20 20"><rect width="20" height="20" rx="3" fill="#222831"/><path d="M6 4l2.5 0 1 3.5-1.6 1.2a8 8 0 0 0 3.4 3.4l1.2-1.6 3.5 1v2.5c0 .6-.5 1-1 1A11 11 0 0 1 5 5c0-.6.4-1 1-1z" fill="#fff"/></svg>
      012-4578-3160
    </span>
    <span class="login">
      <svg width="24" height="24" viewBox="0 0 24 24"><circle cx="12" cy="12" r="10.5" fill="none" stroke="#1c4f8c" stroke-width="2"/><circle cx="12" cy="9.5" r="3.5" fill="#1c4f8c"/><path d="M5.5 18.5a7.5 5 0 0 1 13 0" fill="#1c4f8c"/></svg>
      LOGIN
    </span>
  </div>
  <nav class="main-nav">
    <span class="active">HOME</span><span>ABOUT</span><span>TECHNOLOGY</span><span>BLOG</span><span>CONTACT</span>
  </nav>
</header>

<section class="hero">
  <div class="hero-photo" role="img" aria-label="Photo of an American semi truck with trailer on a highway beside green hills"></div>
  <div class="hero-mark">RIVOLEX</div>
  <p class="hero-copy">We Offer Quality And Reliablity.<br>we’ve Got You And Your<br>Business Covered Day &amp; Night,<br>From Origin To Destination.</p>
  <div class="quote-btn">
    <svg width="26" height="28" viewBox="0 0 26 28" fill="none" stroke="#fff" stroke-width="2"><path d="M3 2h13l6 6v18H3z"/><path d="M7 12h11M7 17h11M7 22h7"/></svg>
    Get A Quote
    <svg width="18" height="14" viewBox="0 0 18 14" fill="none" stroke="#fff" stroke-width="2.4"><path d="M2 2l5 5-5 5M10 2l5 5-5 5"/></svg>
  </div>
</section>

<section class="welcome">
  <h1 class="section-title"><b>Welcome To Rivolex</b> Consulting</h1>
  <div class="divider"><i></i>
    <svg width="18" height="18" viewBox="0 0 18 18" fill="#1c4f8c"><rect x="0" y="0" width="4" height="4"/><rect x="7" y="0" width="4" height="4"/><rect x="14" y="0" width="4" height="4"/><rect x="0" y="7" width="4" height="4"/><rect x="7" y="7" width="4" height="4"/><rect x="14" y="7" width="4" height="4"/><rect x="0" y="14" width="4" height="4"/><rect x="7" y="14" width="4" height="4"/><rect x="14" y="14" width="4" height="4"/></svg>
  <i></i></div>
  <p class="mission">Our mission is to provide our clients with safe, consistent and quality transportation solutions. Our logistics team<br>is committed to customer satisfaction, safety and trust. You can be sure your goods will be delivered on time<br>and in the best condition.</p>
  <p class="priority">At Kestrel Freight customer satisfaction it’s our priority.</p>
  <div class="pill-btn">READ MORE</div>
</section>

<section class="solutions">
  <div class="scene" role="img" aria-label="Photo of a truck on a highway through wooded hills, tinted blue"></div>
  <h2 class="section-title">Solution We Provide</h2>
  <div class="divider"><i></i>
    <svg width="18" height="18" viewBox="0 0 18 18" fill="#fff"><rect x="0" y="0" width="4" height="4"/><rect x="7" y="0" width="4" height="4"/><rect x="14" y="0" width="4" height="4"/><rect x="0" y="7" width="4" height="4"/><rect x="7" y="7" width="4" height="4"/><rect x="14" y="7" width="4" height="4"/><rect x="0" y="14" width="4" height="4"/><rect x="7" y="14" width="4" height="4"/><rect x="14" y="14" width="4" height="4"/></svg>
  <i></i></div>

  <div class="hub">RIVOLEX</div>

  <div class="service" style="left:460px;top:171px">
    <div class="ring"><svg width="40" height="28" viewBox="0 0 40 28"><rect x="2" y="4" width="36" height="16" fill="#fff"/><circle cx="10" cy="24" r="3" fill="#fff"/><circle cx="30" cy="24" r="3" fill="#fff"/></svg></div>
    INTERMODAL
  </div>
  <div class="service" style="left:719px;top:171px">
    <div class="ring"><svg width="34" height="38" viewBox="0 0 34 38" fill="none" stroke="#fff" stroke-width="2.5"><path d="M22 4a7 7 0 0 1 7 7c0 5-7 12-7 12s-7-7-7-12a7 7 0 0 1 7-7z"/><circle cx="22" cy="11" r="2.4" fill="#fff"/><path d="M22 23c-4 6-16 2-12 9"/><circle cx="9" cy="33" r="2.5" fill="#fff"/></svg></div>
    LONG HAUL
  </div>
  <div class="service" style="left:364px;top:339px">
    <div class="ring"><svg width="42" height="30" viewBox="0 0 42 30"><rect x="2" y="3" width="24" height="17" fill="none" stroke="#fff" stroke-width="2.5"/><path d="M26 9h8l6 6v5H26z" fill="#fff"/><circle cx="10" cy="24" r="3.5" fill="#fff"/><circle cx="33" cy="24" r="3.5" fill="#fff"/></svg></div>
    LTL
  </div>
  <div class="service" style="left:822px;top:339px">
    <div class="ring"><svg width="30" height="40" viewBox="0 0 30 40" fill="none" stroke="#fff" stroke-width="2.5"><path d="M11 4h8v22a8 8 0 1 1-8 0z"/><circle cx="15" cy="32" r="3" fill="#fff"/><path d="M15 14v15"/></svg></div>
    TEMP-CONTROL
  </div>
  <div class="service" style="left:450px;top:522px">
    <div class="ring"><svg width="44" height="28" viewBox="0 0 44 28"><rect x="2" y="14" width="26" height="4" fill="#fff"/><path d="M28 6h8l6 6v8H28z" fill="#fff"/><circle cx="10" cy="23" r="3.5" fill="#fff"/><circle cx="35" cy="23" r="3.5" fill="#fff"/></svg></div>
    FLATBED
  </div>
  <div class="service" style="left:729px;top:522px">
    <div class="ring"><svg width="38" height="34" viewBox="0 0 38 34"><rect x="4" y="6" width="30" height="22" rx="2" fill="none" stroke="#fff" stroke-width="2.5"/><path d="M4 14h30M15 6v8M23 6v8" stroke="#fff" stroke-width="2.5"/></svg></div>
    SHORT HAUL
  </div>
</section>

<section class="sectors">
  <div class="sectors-panel">
    <h2>INDUSTRY SECTORS COVERAGE</h2>
    <div class="rule"></div>
    <p class="lead">We cover different industry sectors, from food and beverage, chemical, retail, durable goods and more. Check the full list.</p>
    <ul class="sector-list">
      <li><svg viewBox="0 0 40 36" fill="#fff"><path d="M20 2l12 6-12 6-12-6z"/><path d="M8 14l12 6 12-6v6l-12 6-12-6z"/><path d="M8 26l12 6 12-6v3l-12 6-12-6z"/></svg>Consumer Packaged Goods</li>
      <li><svg viewBox="0 0 40 36" fill="#fff"><path d="M12 4h16v6l6 8v14H6V18l6-8z"/><circle cx="20" cy="23" r="5" fill="#2b323c"/></svg>Chemical Goods</li>
      <li><svg viewBox="0 0 40 36" fill="#fff"><rect x="4" y="10" width="10" height="24" rx="3"/><rect x="7" y="2" width="4" height="8"/><ellipse cx="28" cy="10" rx="9" ry="4"/><rect x="19" y="10" width="18" height="24" rx="4"/></svg>Food and Beverage</li>
      <li><svg viewBox="0 0 40 36" fill="#fff"><path d="M13 2l7 5 7-5 9 6-4 8-3-2v20H11V14l-3 2-4-8z"/></svg>Retail Goods</li>
      <li><svg viewBox="0 0 40 36" fill="#fff"><rect x="2" y="10" width="26" height="16" rx="8"/><path d="M28 12h6l4 6v8H28z"/><circle cx="10" cy="30" r="4"/><circle cx="32" cy="30" r="4"/></svg>Energy, Oil and Gas</li>
    </ul>
  </div>
  <div class="sectors-photo" role="img" aria-label="Photo of a white American semi truck parked on an open road"></div>
  <div class="notch"></div>
</section>

<section class="partners" aria-label="Partners">
  <div class="partner" style="left:92px;width:148px"></div>
  <div class="partner" style="left:266px;width:144px"></div>
  <div class="partner" style="left:448px;width:126px"></div>
  <div class="partner" style="left:634px;width:102px"></div>
  <div class="partner" style="left:800px;width:118px"></div>
  <div class="partner" style="left:958px;width:148px"></div>
</section>

<footer class="site-footer">
  <div class="col" style="left:93px">
    <h3>NEWSLETTER SUBSCRIBE</h3>
    <p>Subscribe to our newsletter and we will inform you about newest projects and promotions.</p>
    <div class="newsletter-form">
      <div class="field">Your email...</div>
      <div class="send"><svg width="14" height="11" viewBox="0 0 14 11"><rect width="14" height="11" fill="#fff"/><path d="M0 0l7 6 7-6" fill="none" stroke="#1f73c6" stroke-width="1.6"/></svg></div>
    </div>
  </div>
  <div class="col" style="left:370px">
    <h3>QUICK LINKS</h3>
    <ul><li>About us</li><li>Company history</li><li>Company Events</li><li>Supply chain management</li><li>Warehousing</li><li>Company news</li><li>Online driver application</li></ul>
  </div>
  <div class="col" style="left:647px">
    <h3>INDUSTRY SOLUTIONS</h3>
    <ul><li>Overland transportation</li><li>Air freight</li><li>Ocean freight</li><li>Large projects</li><li>Rail international shipping</li><li>Contract logistics</li><li>Packaging options</li></ul>
  </div>
  <div class="col contact" style="left:925px">
    <h3>CONTACT US</h3>
    <p>48 Harbor Row,<br>Newark, New Jersey</p>
    <p class="phone">+1-4152-8830-7</p>
    <p class="mail">info@rivolex.com</p>
    <div class="socials"><i></i><i></i><i></i></div>
  </div>
</footer>
<div class="copyright">© 2017. Rivolex.</div>

</body>
</html>
```